New Zealand Marlborough Sauvignon Blanc wine packaging design

We need packaging design for our new wine brand, Halloway Brisk. The wine is a New Zealand Marlborough Sauvignon Blanc. We would like the packaging will portray elegance and style with an understated label. We are looking for a label that portrays the elegance of the French Riviera. The label should be round or pill shaped.

Industry/Entity Type

Wine

Font styles to use
Serif
Sans Serif

Requirements
Must have
• The words in order of importance: Halloway Brisk, Sauvignon Blanc, Marlborough, New Zealand. It should be fit to the bottle posted in the links
Nice to have
• a pill shape or circular shape
Should not have
• Illustrations of wine bottles, wine glasses, or grapes

```html
<!DOCTYPE html>
<html lang="en">
<head>
<meta charset="utf-8">
<title>Halloway Brisk Sauvignon Blanc – Label</title>
<link href="https://fonts.googleapis.com/css2?family=Marcellus&family=Montserrat:wght@500&display=swap" rel="stylesheet">
<style>
  :root {
    --ink-black: #000000;
    --label-white: #ffffff;
    --sky-teal: #1fa6c4;
    --sunset-orange: #f08a3c;
    --sea-turquoise: #2ec1cf;
    --sand-peach: #f2b585;
    --shore-violet: #7c5c8a;
  }
  html, body {
    margin: 0;
    padding: 0;
    width: 705px;
    height: 1200px;
    overflow: hidden;
    background: var(--ink-black);
  }
  .label {
    display: block;
    width: 705px;
    height: 1200px;
  }
  .region-arc {
    font-family: "Montserrat", sans-serif;
    font-weight: 500;
    font-size: 22px;
    letter-spacing: 3px;
    fill: var(--label-white);
  }
  .brand-name {
    font-family: "Marcellus", serif;
    font-size: 60px;
    fill: var(--label-white);
    text-anchor: middle;
  }
  .varietal {
    font-family: "Montserrat", sans-serif;
    font-weight: 500;
    font-size: 15px;
    letter-spacing: 14px;
    fill: var(--label-white);
    text-anchor: middle;
  }
</style>
</head>
<body>
<svg class="label" viewBox="0 0 705 1200" xmlns="http://www.w3.org/2000/svg">
  <defs>
    <linearGradient id="riviera-scene-tones" x1="0" y1="0" x2="0" y2="1">
      <stop offset="0" stop-color="var(--sky-teal)"/>
      <stop offset="0.26" stop-color="#4fb3c6"/>
      <stop offset="0.36" stop-color="var(--sunset-orange)"/>
      <stop offset="0.42" stop-color="var(--shore-violet)"/>
      <stop offset="0.5" stop-color="var(--sea-turquoise)"/>
      <stop offset="0.62" stop-color="#1f8fb0"/>
      <stop offset="0.72" stop-color="var(--sand-peach)"/>
      <stop offset="1" stop-color="#e9925a"/>
    </linearGradient>
    <path id="region-arc-path" d="M188,410 A172,205 0 0,1 516,410"/>
  </defs>

  <text class="region-arc">
    <textPath href="#region-arc-path" startOffset="50%" text-anchor="middle">NEW ZEALAND MARLBOROUGH</textPath>
  </text>

  <ellipse class="scene-oval" cx="352" cy="470" rx="148" ry="178"
           fill="url(#riviera-scene-tones)"
           role="img" aria-label="Illustration of a Riviera beach at sunset with sea, clouds, parasols and seaside villas"/>

  <text class="brand-name" x="352" y="705">HALLOWAY</text>
  <text class="brand-name" x="352" y="752">BRISK</text>
  <text class="varietal" x="359" y="790">SAUVIGNON BLANC</text>
</svg>
</body>
</html>
```